New Labels for VANTO Sports Drinks

Sports drink company looking for new fresh look with commercial appeal beverage labels. You can use the current label as a guide but adjust where you see fit. Would like to standout from other sports drink on store shelves. VANTO Sports Drinks is a fusion of real brewed tea and all natural electrolytes. Our tea features a bold, full-bodied flavor profile, combined with all natural electrolytes, giving you one of the very first tea based sports drinks.

Target Market(s)

16-40

Colors

Designer to choose colors to be used in the design.

Requirements
Must have
• Name
• flavor
• description
• nutritional info
• all Info on back of labels
Nice to have
• sports image
• fruit flavor
• white background
• Real tea and natural electrolytes
Should not have
• n/a

```html
<!DOCTYPE html>
<html lang="en">
<head>
<meta charset="utf-8">
<title>VANTO Sports Tea – Lemon Label</title>
<link href="https://fonts.googleapis.com/css2?family=Black+Ops+One&family=Tinos&display=swap" rel="stylesheet">
<style>
  :root {
    --ink: #111111;
    --paper: #ffffff;
    --backdrop: #ededed;
    --lemon: #f5ef1a;
    --haze: #e4e4e4;
    --haze-soft: #f3f3f3;
  }
  html, body {
    margin: 0;
    padding: 0;
    width: 1200px;
    height: 943px;
    overflow: hidden;
    background: var(--backdrop);
  }
  .label {
    position: absolute;
    left: 237px;
    top: 48px;
    width: 726px;
    height: 847px;
    background: var(--paper);
    overflow: hidden;
    font-family: "Black Ops One", "Arial Black", sans-serif;
    color: var(--ink);
  }
  .sports-backdrop {
    position: absolute;
    left: 0;
    top: 150px;
    width: 726px;
    height: 500px;
    background: radial-gradient(closest-side, var(--haze) 0%, var(--haze-soft) 60%, var(--paper) 100%);
  }
  .flavor {
    position: absolute;
    top: 8px;
    left: 0;
    width: 726px;
    text-align: center;
    font-size: 50px;
    line-height: 56px;
    letter-spacing: 1px;
  }
  .tagline-band {
    position: absolute;
    top: 74px;
    left: 0;
    width: 726px;
    height: 58px;
    background: var(--ink);
    color: var(--paper);
    font-size: 34px;
    line-height: 58px;
    text-align: center;
    letter-spacing: 1px;
  }
  .brand-mark {
    position: absolute;
    top: 168px;
    left: 288px;
    width: 150px;
    height: 150px;
    background: var(--lemon);
  }
  .brand-name {
    position: absolute;
    top: 290px;
    left: 0;
    width: 726px;
    text-align: center;
    font-size: 200px;
    line-height: 1;
    color: var(--ink);
  }
  .base-panel {
    position: absolute;
    left: 0;
    top: 612px;
    width: 726px;
    height: 235px;
  }
  .product-type {
    position: absolute;
    top: 680px;
    left: 0;
    width: 726px;
    text-align: center;
    color: var(--paper);
    font-size: 74px;
    line-height: 84px;
    letter-spacing: 2px;
  }
  .volume {
    position: absolute;
    top: 778px;
    left: 0;
    width: 726px;
    text-align: center;
    color: var(--paper);
    font-family: "Tinos", "Times New Roman", serif;
    font-size: 28px;
  }
</style>
</head>
<body>
  <main class="label">
    <div class="sports-backdrop" role="img" aria-label="Faint background graphic of an athlete in motion"></div>
    <div class="flavor">LEMON</div>
    <div class="tagline-band">TEA &amp; ELECTROLYTES</div>
    <span class="brand-mark"></span>
    <div class="brand-name">VANTO</div>
    <svg class="base-panel" viewBox="0 0 726 235" aria-hidden="true">
      <polygon points="0,14 120,0 726,20 726,235 0,235" fill="var(--ink)"/>
    </svg>
    <div class="product-type">SPORTS TEA</div>
    <div class="volume">16 fl. oz. (474ml)</div>
  </main>
</body>
</html>
```